Prairie Hollow - responsive bootstrap website design

Looking to build a responsive service website.

Logo has been provided.

PLEASE REVIEW ATTACHED DESIGN STYLE GUIDES & CLIENT CREATIVE BRIEF FOR OUR REQUIREMENT.

THANK YOU AND GOOD LUCK!

```html
<!DOCTYPE html>
<html lang="en">
<head>
<meta charset="utf-8">
<title>Prairie Hollow Outfitters</title>
<link href="https://fonts.googleapis.com/css2?family=Arvo:wght@400;700&family=Lato:wght@400;700&family=Dancing+Script:wght@600&display=swap" rel="stylesheet">
<style>
:root{
  --teal:#2aaecf;
  --teal-dark:#1f93b0;
  --ink:#1c1c1c;
  --text:#333;
  --muted:#888;
  --black:#0d0d0d;
  --footer:#111;
  --bar:#3a3a3a;
  --white:#fff;
}
*{box-sizing:border-box;margin:0;padding:0}
html,body{width:756px;height:1200px;overflow:hidden;background:var(--white)}
body{position:relative;font-family:'Lato',sans-serif;color:var(--text)}
.abs{position:absolute}
.slab{font-family:'Arvo',serif}

/* header */
.site-header{left:0;top:0;width:756px;height:64px;background:linear-gradient(#1a1a1a,#050505)}
.nav{top:42px;font-family:'Arvo',serif;font-size:7.5px;color:var(--white);display:flex}
.nav a{color:inherit;text-decoration:none;padding:0 14px;border-left:1px dotted #666}
.nav a:first-child{border-left:none;padding-left:0}
.nav a.active{color:var(--teal)}
.brand{left:300px;top:8px;width:156px;text-align:center;color:var(--white);font-family:'Arvo',serif;font-size:13px;line-height:16px}
.social{right:108px;top:10px;display:flex;gap:3px}
.social span{width:13px;height:13px;border-radius:50%;background:var(--teal);display:block}

/* hero */
.hero{left:0;top:64px;width:756px;height:321px;background:linear-gradient(180deg,#c9d3db 0%,#e2e7ea 55%,#8e9ba6 82%,#5f6e7a 100%)}
.hero h1{left:108px;top:84px;font-family:'Arvo',serif;font-weight:400;font-size:25px;line-height:27px;color:var(--ink)}
.hero p{left:109px;top:143px;width:260px;font-size:7.5px;line-height:10.5px;color:#222}
.btn{left:108px;top:183px;width:129px;height:25px;background:var(--teal);color:var(--white);font-family:'Arvo',serif;font-size:8px;display:flex;align-items:center;padding-left:10px}
.btn svg{position:absolute;right:8px;top:6px}
.hero-photo{left:350px;top:0;width:390px;height:321px;background:radial-gradient(ellipse at 55% 45%,rgba(240,190,180,.55),rgba(200,210,215,0) 60%)}
.dots{left:356px;top:301px;display:flex;gap:4px}
.dots span{width:12px;height:12px;background:#111;display:block}
.dots span:first-child{background:var(--teal)}

.divider{left:0;width:756px;height:14px;background:radial-gradient(ellipse at 50% 0%,rgba(0,0,0,.12),rgba(0,0,0,0) 70%)}

/* welcome */
.welcome-title{left:0;top:412px;width:756px;text-align:center;font-family:'Arvo',serif;font-size:15px;color:var(--teal)}
.welcome-text{left:118px;top:443px;width:520px;text-align:center;font-size:7.5px;line-height:10px;color:#222}

/* guide */
.section-title{font-family:'Arvo',serif;font-size:14.5px;color:var(--teal)}
.guide-photo{left:109px;top:562px;width:95px;height:134px;border:2px solid #bbb;border-radius:5px;background:linear-gradient(180deg,#7c8f80,#9aa39a 50%,#6d6a5e)}
.guide-text{left:219px;top:561px;width:285px;font-size:7.2px;line-height:9.8px;color:#333}
.guide-text a{color:var(--teal);text-decoration:none}
.widget-title{left:530px;top:531px;font-family:'Arvo',serif;font-size:11px;color:var(--ink)}
.widget{left:545px;top:562px;width:94px;height:134px;background:#3d5a80;border:1px solid #2b4263;border-radius:3px;color:var(--white);font-size:5px}
.widget .chart{position:absolute;left:3px;top:75px;width:86px;height:50px;background:var(--white)}

/* columns */
.col-head{top:751px;width:171px;height:24px;background:var(--teal);color:var(--white);font-family:'Arvo',serif;font-size:11px;display:flex;align-items:center;padding-left:8px;gap:8px}
.thumb{width:52px;height:52px}
.news-item{left:295px;width:162px;display:flex;gap:7px;border-bottom:1px solid #ddd;padding-bottom:6px}
.date{width:16px;height:25px;background:var(--teal);color:var(--white);text-align:center;font-family:'Arvo',serif;font-size:10px;line-height:12px;flex:none}
.date small{display:block;font-size:4.5px;line-height:6px}
.news-item h4{font-family:'Arvo',serif;font-weight:400;font-size:7.5px;color:var(--teal-dark)}
.news-item p{font-family:'Arvo',serif;font-size:5.5px;line-height:7.5px;color:var(--muted)}
.blog-photo{left:478px;top:786px;width:169px;height:52px;border-radius:3px;background:linear-gradient(180deg,#5c6c85,#9aa5bd 45%,#c6c3d0 60%,#5d6a80)}
.blog-meta{left:479px;top:845px;width:168px;display:flex;justify-content:space-between;font-family:'Arvo',serif;font-size:5.8px;color:var(--teal-dark)}
.blog-text{left:479px;top:859px;width:168px;font-family:'Arvo',serif;font-size:5.8px;line-height:8px;color:var(--muted)}

/* partners */
.partner{background:#9a9a9a}

/* footer */
.site-footer{left:0;top:1033px;width:756px;height:136px;background:var(--footer);color:#bbb}
.foot-title{font-family:'Arvo',serif;font-size:11px;color:var(--teal)}
.foot-list{font-family:'Arvo',serif;font-size:7px;line-height:12.3px;color:#bbb;list-style:none}
.contact-row{left:108px;display:flex;gap:6px;font-family:'Arvo',serif;font-size:7px;line-height:12px;color:#bbb}
.foot-brand{left:556px;top:20px;width:92px;text-align:center;font-family:'Arvo',serif;font-size:11px;line-height:13px;color:#ccc}
.foot-social{left:568px;top:55px;display:flex;gap:3px}
.foot-social span{width:13px;height:13px;border-radius:50%;background:#777;display:block}
.copy{left:0;top:1169px;width:756px;height:31px;background:var(--bar);color:#bbb;font-size:6.5px;line-height:9px;text-align:center;padding-top:6px}
</style>
</head>
<body>

<header class="abs site-header">
  <nav class="abs nav" style="left:110px">
    <a class="active">Home</a><a>About Us</a><a>Guide</a><a>Services</a>
  </nav>
  <div class="abs brand">Prairie Hollow<br>Outfitters</div>
  <nav class="abs nav" style="left:442px">
    <a>Merchandise</a><a>Video</a><a>Picture</a><a>Gallery</a>
  </nav>
  <div class="abs social"><span></span><span></span><span></span><span></span></div>
</header>

<section class="abs hero">
  <div class="abs hero-photo" role="img" aria-label="Angler on a boat holding up a red snapper and a fishing rod, with open sea and clouds behind"></div>
  <h1 class="abs">Pure Prairie Hollow<br>Prime Time</h1>
  <p class="abs">Lorem ipsum dolor sit amet, costuer aipiscing elit, sed diam noummy nibh euismod tincunt ut laoreet dolore magna aliquam erat volutpat. Ut wisi enim ad minim veniam,.</p>
  <div class="abs btn">CLICK FOR DETAL
    <svg width="13" height="13" viewBox="0 0 13 13"><circle cx="6.5" cy="6.5" r="5.8" fill="none" stroke="#fff" stroke-width="1"/><path d="M5.5 4 L8 6.5 L5.5 9" fill="none" stroke="#fff" stroke-width="1"/></svg>
  </div>
  <div class="abs dots"><span></span><span></span><span></span></div>
</section>

<h2 class="abs welcome-title">Welcome to Prairie Hollow Outfitters</h2>
<p class="abs welcome-text">Lowcountry's own Prairie Hollow Outfitters is your ultimate destination for saltwater fishing. From fly fishing for tailing reds in a foot of water to chasing Pelagic in the Gulf Stream, here you'll find all the gear, apparel, and expert advice you'll need to make the most of your time on the water.</p>
<div class="abs divider" style="top:474px"></div>

<h2 class="abs section-title" style="left:109px;top:530px">Guide Services at Prairie Hollow Outfitters</h2>
<div class="abs guide-photo" role="img" aria-label="Three anglers on a dock beside a large hanging tuna"></div>
<div class="abs guide-text">
  <p>Looking for guidance? Prairie Hollow Outfitters provides professional guide services featuring the areas' best captains and crews.</p><br>
  <p>Regardless of your skill level or experience, we can accommodate your group to create an exhilarating and memorable fishing experience. <a>more ...</a></p>
</div>
<div class="abs widget-title">Tide Chart<sup style="font-size:5px">TM</sup> Widget</div>
<div class="abs widget">
  <div class="abs" style="left:7px;top:6px;font-size:5.5px;line-height:7px">7/24/14<br>2:36 pm</div>
  <svg class="abs" style="left:36px;top:3px" width="20" height="22" viewBox="0 0 20 22"><path d="M10 1 L19 11 H14 V21 H6 V11 H1 Z" fill="#22c52e"/></svg>
  <div class="abs" style="left:38px;top:27px">Rising</div>
  <div class="abs" style="right:6px;top:12px;font-size:8px">0.9'</div>
  <div class="abs" style="right:6px;top:24px;text-align:right;line-height:6px">Rate<br>1.2/hr</div>
  <div class="abs" style="left:4px;top:40px;width:86px;line-height:6px">Reed Cay, Willow Creek, Harbor Point, South Carolina</div>
  <div class="abs" style="left:4px;top:60px;line-height:6px">High 7:14 AM, 7:56 PM<br>Low 1:16 AM, 1:18 PM</div>
  <div class="chart">
    <svg width="86" height="50" viewBox="0 0 86 50"><path d="M4 44 C14 44 18 8 26 8 C34 8 38 44 46 44 C54 44 58 8 66 8 C74 8 78 44 84 44 Z" fill="#1a6ed8"/><line x1="4" y1="44" x2="84" y2="44" stroke="#999" stroke-width=".5"/><circle cx="55" cy="38" r="3" fill="#cde" stroke="#667" stroke-width=".5"/></svg>
  </div>
</div>
<div class="abs divider" style="top:730px"></div>

<div class="abs col-head" style="left:108px">
  <svg width="17" height="13" viewBox="0 0 17 13"><rect x="1" y="1" width="15" height="11" fill="none" stroke="#fff" stroke-width="1.2"/><path d="M2 11 L7 6 L10 9 L12 7 L15 11" fill="none" stroke="#fff"/><circle cx="11" cy="4" r="1.3" fill="#fff"/></svg>Photo Gallery</div>
<div class="abs col-head" style="left:292px">
  <svg width="14" height="14" viewBox="0 0 14 14"><rect x="1" y="1" width="12" height="12" fill="none" stroke="#fff"/><path d="M3 4H11M3 7H11M3 10H11" stroke="#fff"/></svg>News</div>
<div class="abs col-head" style="left:477px">
  <svg width="15" height="14" viewBox="0 0 15 14"><rect x="1" y="2" width="10" height="11" fill="none" stroke="#fff"/><path d="M4 1H14V10" fill="none" stroke="#fff"/></svg>Blog</div>

<div class="abs thumb" style="left:108px;top:787px;background:linear-gradient(#4f86b5,#3f7a3f)" role="img" aria-label="Angler holding a mahi on a boat"></div>
<div class="abs thumb" style="left:167px;top:787px;background:linear-gradient(#5b8fc0,#b4a24c)" role="img" aria-label="Angler with a dorado catch"></div>
<div class="abs thumb" style="left:224px;top:787px;background:linear-gradient(#e7d9c4,#2a2a2a)" role="img" aria-label="Silhouetted fishers at sunset"></div>
<div class="abs thumb" style="left:108px;top:846px;background:linear-gradient(#a9c3d4,#5b4b3a)" role="img" aria-label="Angler with a catch near the water"></div>
<div class="abs thumb" style="left:167px;top:846px;background:linear-gradient(#cfe0ea,#3f6e8a)" role="img" aria-label="Charter boat at the dock"></div>
<div class="abs thumb" style="left:224px;top:846px;background:linear-gradient(#8fc4e3,#c9b07a)" role="img" aria-label="Angler on a beach with a fish"></div>

<div class="abs news-item" style="top:786px"><div class="date">23<small>JUL</small></div><div><h4>searchable version</h4><p>A fully searchable A-Z version of the newsroom style guide that is designed t</p></div></div>
<div class="abs news-item" style="top:832px"><div class="date">23<small>JUL</small></div><div><h4>searchable version</h4><p>A fully searchable A-Z version of the newsroom style guide that is designed</p></div></div>
<div class="abs news-item" style="top:874px;border-bottom:none"><div class="date">23<small>JUL</small></div><div><h4>searchable version</h4><p>A fully searchable A-Z version of the newsroom style guide that is designed</p></div></div>

<div class="abs blog-photo" role="img" aria-label="Rods on a boat at dusk over calm water"></div>
<div class="abs blog-meta"><span>Dana Reyes</span><span>25/07/2014</span></div>
<p class="abs blog-text">Lorem ipsum dolor sit amet, consectetuer adipiscing elit, sed diam nonummy dolore magna aliquam erat volutpat.</p>
<div class="abs divider" style="top:922px"></div>

<div class="abs partner" style="left:110px;top:958px;width:55px;height:42px;border-radius:4px"></div>
<div class="abs partner" style="left:180px;top:960px;width:40px;height:40px;border-radius:50%"></div>
<div class="abs partner" style="left:240px;top:962px;width:67px;height:36px"></div>
<div class="abs partner" style="left:325px;top:962px;width:160px;height:36px"></div>
<div class="abs partner" style="left:506px;top:962px;width:74px;height:38px"></div>
<div class="abs partner" style="left:600px;top:960px;width:47px;height:42px;border-radius:50%"></div>

<footer class="abs site-footer">
  <h3 class="abs foot-title" style="left:109px;top:16px">Contact Us</h3>
  <div class="abs contact-row" style="top:43px">
    <svg width="12" height="14" viewBox="0 0 12 14"><path d="M6 1 C3 1 1.5 3 1.5 5.5 C1.5 8.5 6 13 6 13 C6 13 10.5 8.5 10.5 5.5 C10.5 3 9 1 6 1 Z" fill="none" stroke="#aaa"/><circle cx="6" cy="5.5" r="1.6" fill="#aaa"/></svg>
    <span>Prairie Hollow Outfitters Capt. Wade<br>Harlan, Owner 4820 Marsh Creek Road,<br>Suite 210 Harbor Point, SC 29900</span>
  </div>
  <div class="abs contact-row" style="top:83px">
    <svg width="12" height="10" viewBox="0 0 12 10"><path d="M1 4 C1 1 11 1 11 4 L9 5 L8 3 H4 L3 5 Z M3 6 H9 V9 H3 Z" fill="none" stroke="#aaa"/></svg><span>555-014-2210</span></div>
  <div class="abs contact-row" style="top:105px">
    <svg width="12" height="10" viewBox="0 0 12 10"><rect x="1" y="2" width="10" height="7" fill="none" stroke="#aaa"/><path d="M3 2V0.5H9V2" fill="none" stroke="#aaa"/></svg><span>555-014-2231</span></div>

  <h3 class="abs foot-title" style="left:325px;top:16px">Fishing Tips</h3>
  <ul class="abs foot-list" style="left:325px;top:42px"><li>Tips Home</li><li>Bass Fishing</li><li>Tips Saltwater</li><li>Tips Species</li><li>Finder Fishing</li><li>FAQ</li></ul>
  <h3 class="abs foot-title" style="left:439px;top:16px">Travel Guides</h3>
  <ul class="abs foot-list" style="left:440px;top:42px"><li>Travel Home</li><li>Florida Louisiana</li><li>Newfoundland</li><li>Fishing Guides</li></ul>

  <div class="abs foot-brand">Prairie Hollow<br>Outfitters</div>
  <div class="abs foot-social"><span></span><span></span><span></span><span></span></div>
</footer>
<div class="abs copy">Site Copyright © 2012 Prairie Hollow Outfitters. | www.prairiehollowoutfitters.com<br>Please e-mail us if you have any questions or comments about this site.</div>

</body>
</html>
```